Tallowgate wool harvest company

We are sheep shearing contractors,we are looking for a simple design business card, with a drawing like picture of a Australian sheep on it, then just standard details, name, phone, email, po box.
We would like double sided, with 2 lines of wiriting on the back, no bright colours please.
We like black and white, doesn't have to be too serious, however nothing to far left of cwntre.
On the back of the card we would like professional shearing contract offering full contract team.
Can use use the symbol & in the name instead of and.

Target Market(s)

Sheep farmers, target males from age 20 and up

Contact Information for Business Card

Company name ram and u fleece works pty ltd
Darren pomfield 0477315846, po box 2741 sale vic 3853,
Email tallowgate@mailnest.example, gippsland shearing contractor

Font styles to use
Serif

Colors

Designer to choose only greyscale colors for use in the design.

Requirements
Nice to have
• Simple design

```html
<!DOCTYPE html>
<html lang="en">
<head>
<meta charset="utf-8">
<title>Tallowgate wool harvest company – business card</title>
<link rel="stylesheet" href="https://fonts.googleapis.com/css2?family=Lora:wght@400;700&display=swap">
<style>
  :root {
    --backdrop: #222222;
    --card-light: #ffffff;
    --card-dark: #1d1d1d;
    --ink-dark: #1a1a1a;
    --ink-light: #f4f4f4;
    --rule-grey: #8a8a8a;
    --art-tint: #ececec;
  }
  * { box-sizing: border-box; margin: 0; padding: 0; }
  html, body { width: 1200px; height: 1200px; overflow: hidden; }
  body {
    background: var(--backdrop);
    font-family: "Lora", Georgia, serif;
    display: flex;
    flex-direction: column;
    align-items: center;
    justify-content: center;
    gap: 60px;
  }
  .card {
    position: relative;
    width: 900px;
    height: 500px;
    box-shadow: 0 14px 40px rgba(0,0,0,0.5);
    overflow: hidden;
  }

  /* Back side: writing lines */
  .card--back { background: var(--card-light); color: var(--ink-dark); }
  .card-art {
    position: absolute;
    left: 340px; top: 70px;
    width: 400px; height: 400px;
    border-radius: 48% 42% 40% 50%;
    background: radial-gradient(ellipse at 50% 50%, var(--art-tint) 0%, rgba(236,236,236,0.5) 55%, rgba(255,255,255,0) 75%);
  }
  .write-line {
    position: absolute;
    left: 150px; right: 70px;
    height: 1.5px;
    background: var(--rule-grey);
  }
  .write-line:nth-of-type(2) { top: 140px; }
  .write-line:nth-of-type(3) { top: 195px; }
  .write-line:nth-of-type(4) { top: 250px; }
  .card--back .brand-name {
    position: absolute;
    left: 340px; width: 400px;
    top: 340px;
    text-align: center;
  }

  .brand-name {
    font-weight: 700;
    line-height: 1.15;
  }
  .brand-name .brand-main { display: block; font-size: 44px; }
  .brand-name .brand-sub { display: block; font-size: 21px; }

  /* Front side: contact details */
  .card--front { background: var(--card-dark); color: var(--ink-light); }
  .card--front .brand-name {
    position: absolute;
    left: 40px; width: 380px;
    top: 150px;
    text-align: center;
  }
  .divider {
    position: absolute;
    left: 450px; top: 110px;
    width: 1.5px; height: 240px;
    background: var(--ink-light);
  }
  .contact {
    position: absolute;
    left: 490px; top: 120px;
  }
  .contact-name { font-size: 36px; font-weight: 700; line-height: 1.1; }
  .contact-role { font-size: 23px; margin-bottom: 30px; }
  .contact-list { list-style: none; font-size: 21px; line-height: 1.45; }
  .contact-list li { display: flex; align-items: center; gap: 14px; }
  .contact-list svg { width: 18px; height: 18px; fill: var(--ink-light); flex: none; }
</style>
</head>
<body>
  <section class="card card--back">
    <div class="card-art" role="img" aria-label="Faint illustration of a shearer holding a sheep"></div>
    <div class="write-line"></div>
    <div class="write-line"></div>
    <div class="write-line"></div>
    <p class="brand-name">
      <span class="brand-main">Tallowgate</span>
      <span class="brand-sub">wool harvest company</span>
    </p>
  </section>

  <section class="card card--front">
    <p class="brand-name">
      <span class="brand-main">Tallowgate</span>
      <span class="brand-sub">wool harvest company</span>
    </p>
    <div class="divider"></div>
    <div class="contact">
      <h1 class="contact-name">Darren pomfield</h1>
      <p class="contact-role">Gippsland shearing contractor</p>
      <ul class="contact-list">
        <li>
          <svg viewBox="0 0 24 24" aria-hidden="true"><path d="M6.6 10.8a15 15 0 0 0 6.6 6.6l2.2-2.2c.3-.3.7-.4 1-.2 1.1.4 2.3.6 3.6.6.6 0 1 .4 1 1V20c0 .6-.4 1-1 1A17 17 0 0 1 3 4c0-.6.4-1 1-1h3.5c.6 0 1 .4 1 1 0 1.3.2 2.5.6 3.6.1.3 0 .7-.2 1z"/></svg>
          <span>0477315846</span>
        </li>
        <li>
          <svg viewBox="0 0 24 24" aria-hidden="true"><path d="M12 2a7 7 0 0 0-7 7c0 5.2 7 13 7 13s7-7.8 7-13a7 7 0 0 0-7-7zm0 9.5A2.5 2.5 0 1 1 12 6.5a2.5 2.5 0 0 1 0 5z"/></svg>
          <span>Po box 2741 sale vic 3853,</span>
        </li>
        <li>
          <svg viewBox="0 0 24 24" aria-hidden="true"><path d="M2 5h20v14H2zm2 2v.5l8 5 8-5V7l-8 5z"/></svg>
          <span>tallowgate@mailnest.example</span>
        </li>
      </ul>
    </div>
  </section>
</body>
</html>
```